Kestrel Arc Services business card Design

I need a business card that will wow clients at first sight.

Kestrel Arc Services connects people with HOME & LIFESTYLE SERVICES, and the client pays the value that was created by our service, using. 'Settle On The Sum That Feels Fair".
Please look us up at www.kestrelarcservices.example to see our mission and services.

The new website is being launched in 8 weeks.

I need a business card to campaign LANDSCAPING however please design it to be easily modified to CLEANING SERVICE, PLUMBING Etc Etc.

Until our SEO campaign begins working I need business cards to leave with prospective clients for each individual service as appropriate.

Dorian Maltby
Creative Director
www.kestrelarcservices.example
1-888-517-4KAS
email: info@kestrelarcservices.example

Target Market(s)

Residential and commercial clients

Industry/Entity Type

Business

Contact Information for Business Card

2 sided

Font styles to use
Sans Serif

Requirements
Must have
• Im prefering a black card so far
• Logo
• "Settle On The Sum That Feels Fair" seal
• Complete Landscaping & Construction
• Tarnwell Services
• Contact details
• facebook kestrelarc services
• twitter @kestrelarc services
• Adaptable card easily to different services we offer at Kestrel Arc Services as per www.kestrelarcservices.example
Should not have
• Too much imagery

```html
<!DOCTYPE html>
<html lang="en">
<head>
<meta charset="utf-8">
<title>Kestrel Arc Services – Business Card</title>
<link rel="stylesheet" href="https://fonts.googleapis.com/css2?family=Open+Sans:wght@300;400;600&display=swap">
<style>
  :root {
    --bg: #d9d4cc;
    --card-black: #050505;
    --card-white: #f4f4f4;
    --ink: #2b2b2b;
    --ink-soft: #6e6e6e;
    --accent-blue: #3f7fd0;
    --accent-violet: #9a63d6;
    --swoosh: #8a8a8a;
    --white: #ffffff;
    --white-soft: #bdbdbd;
  }
  * { margin: 0; padding: 0; box-sizing: border-box; }
  html, body { width: 1200px; height: 1062px; overflow: hidden; }
  body {
    background: var(--bg);
    font-family: "Open Sans", Arial, sans-serif;
    color: var(--ink);
  }
  .sheet {
    position: relative;
    width: 1200px;
    height: 1062px;
    display: flex;
    flex-direction: column;
    align-items: center;
    justify-content: space-evenly;
  }
  .card {
    position: relative;
    width: 840px;
    height: 480px;
    overflow: hidden;
    box-shadow: 0 10px 28px rgba(0,0,0,0.28);
  }
  .card-bg { position: absolute; inset: 0; }

  /* shared brand block */
  .brand {
    display: flex;
    align-items: center;
    gap: 18px;
  }
  .brand-dot {
    width: 34px; height: 34px;
    border-radius: 50%;
    background: var(--accent-blue);
    flex: none;
  }
  .brand-name {
    font-size: 44px;
    font-weight: 400;
    color: var(--ink);
    letter-spacing: -0.5px;
    line-height: 1;
    white-space: nowrap;
  }
  .brand-name small { font-size: 22px; }
  .slogan {
    font-size: 11px;
    letter-spacing: 7px;
    text-transform: uppercase;
    color: var(--accent-blue);
    margin-top: 10px;
    white-space: nowrap;
  }

  /* front */
  .card--front .brand { position: absolute; left: 70px; top: 82px; }
  .person { position: absolute; left: 122px; top: 214px; }
  .person-name { font-size: 30px; font-weight: 600; color: var(--ink); line-height: 1.1; }
  .person-role { font-size: 22px; font-weight: 300; color: var(--ink-soft); }
  .service-line {
    position: absolute;
    left: 122px;
    top: 292px;
    font-size: 12px;
    font-weight: 600;
    letter-spacing: 2px;
    text-transform: uppercase;
    color: var(--accent-blue);
  }

  .contacts {
    position: absolute;
    left: 250px;
    top: 338px;
    list-style: none;
    font-size: 19px;
    color: var(--ink);
  }
  .contacts li { display: flex; align-items: center; gap: 12px; height: 32px; }
  .contacts svg { width: 16px; height: 16px; flex: none; }
  .contacts .at { width: 16px; font-weight: 600; text-align: center; }

  .social {
    position: absolute;
    right: 60px;
    top: 190px;
    text-align: right;
    font-size: 19px;
    color: var(--ink);
    line-height: 30px;
  }

  /* back */
  .card--back .card-bg {
    background: radial-gradient(ellipse at 40% 30%, #2a2a2a 0%, #0b0b0b 55%, #000 100%);
  }
  .back-services {
    position: absolute;
    left: 90px;
    top: 78px;
    color: var(--white);
  }
  .back-services .service-main {
    font-size: 24px;
    font-weight: 300;
    line-height: 1.3;
  }
  .back-services .service-sub {
    font-size: 14px;
    font-weight: 600;
    letter-spacing: 3px;
    text-transform: uppercase;
    color: var(--accent-violet);
    margin-top: 8px;
  }
  .seal {
    position: absolute;
    right: 80px;
    top: 60px;
    width: 120px;
    height: 120px;
  }
  .back-brand {
    position: absolute;
    left: 90px;
    bottom: 90px;
  }
  .back-brand .brand-name { color: var(--white); font-size: 54px; }
  .back-brand .brand-name small { font-size: 26px; }
  .back-brand .slogan { color: var(--white-soft); font-size: 12px; letter-spacing: 8px; margin-top: 14px; }
  .back-brand .brand-dot { width: 40px; height: 40px; }
</style>
</head>
<body>
<main class="sheet">

  <section class="card card--front" aria-label="Business card front">
    <svg class="card-bg" viewBox="0 0 840 480" preserveAspectRatio="none" aria-hidden="true">
      <rect width="840" height="480" fill="var(--card-black)"/>
      <path d="M0,0 H560 Q790,30 840,210 V480 H300 Q70,450 0,300 Z" fill="var(--card-white)"/>
      <path d="M600,6 Q800,50 836,230" fill="none" stroke="var(--swoosh)" stroke-width="3"/>
      <path d="M260,474 Q60,440 4,330" fill="none" stroke="var(--swoosh)" stroke-width="3"/>
    </svg>

    <div class="brand">
      <span class="brand-dot"></span>
      <div>
        <div class="brand-name">Kestrel Arc Services <small>Inc.</small></div>
        <div class="slogan">"Settle on the sum that feels fair"</div>
      </div>
    </div>

    <div class="person">
      <div class="person-name">Add Name</div>
      <div class="person-role">Manager</div>
    </div>

    <div class="service-line">Complete Landscaping &amp; Construction</div>

    <ul class="contacts">
      <li>
        <svg viewBox="0 0 16 16" aria-hidden="true"><path d="M4 1h3l1 4-2 1a9 9 0 0 0 4 4l1-2 4 1v3a2 2 0 0 1-2 2A13 13 0 0 1 2 3a2 2 0 0 1 2-2z" fill="var(--ink)"/></svg>
        1-888-517-4KAS
      </li>
      <li>
        <svg viewBox="0 0 16 16" aria-hidden="true"><g fill="none" stroke="var(--ink)" stroke-width="1.3"><circle cx="8" cy="8" r="6.5"/><ellipse cx="8" cy="8" rx="3" ry="6.5"/><path d="M1.5 8h13M2.5 4.5h11M2.5 11.5h11"/></g></svg>
        www.kestrelarcservices.example
      </li>
      <li><span class="at">@</span>info@kestrelarcservices.example</li>
    </ul>

    <div class="social">
      facebook kestrelarc services<br>
      twitter @kestrelarc services
    </div>
  </section>

  <section class="card card--back" aria-label="Business card back">
    <div class="card-bg"></div>

    <div class="back-services">
      <div class="service-main">Complete Landscaping &amp; Construction</div>
      <div class="service-sub">Tarnwell Services</div>
    </div>

    <svg class="seal" viewBox="0 0 120 120" role="img" aria-label="Settle On The Sum That Feels Fair seal">
      <circle cx="60" cy="60" r="56" fill="var(--accent-blue)"/>
    </svg>

    <div class="back-brand">
      <div class="brand">
        <span class="brand-dot"></span>
        <div>
          <div class="brand-name">Kestrel Arc Services <small>Inc.</small></div>
          <div class="slogan">"Settle on the sum that feels fair"</div>
        </div>
      </div>
    </div>
  </section>

</main>
</body>
</html>
```